Business card design for a dynamic IT consulting company

We need a business card design for a young firm, specialized in the Telecommunications/Consulting industry. The name of the company is Brask and Partners Business Consulting Ltd. (Short name: Brask and Partnes)
Brask = solve read reverse, so we aim to be uncomplicated and solution-oriented. The small pipe in our logo is also related to the word solve. So we need a new business card design, which is simple, eye catching and something non traditional (I would probably prefer a square shaped design rather than a rectangle, but open for suggestions). Attached our logo.

Target Market(s)

Usually our customers are Tier1 Telecoms providers (Q-Linkra, Parnexo, etc) and their executives.

Industry/Entity Type

Business

Contact Information for Business Card

Name: Gergely Halmindo
Email: g.halmindo@braskpartnera.hu
Web: www.braskpartnera.hu
Mobile: +36 30 555 0192
Title: Managing Director

Optional:
Company name: Brask and Partners Ltd.
Address: 1047 Budapest, Ravaszi str. 17/B, Hungary

Font styles to use
Other font styles liked:
• helveticaneue_medium, Prime Regular are used now.

Colors

Designer to choose colors to be used in the design.

Requirements
Must have
• I would like to have a 2 sided design.
Nice to have
• I thought if we make the logo a bit bigger (without the company name), that could go to the back with the company name below. I though, if the pipe in the logo is somehow touchable on the business card, would be nice and unique.

```html
<!DOCTYPE html>
<html lang="en">
<head>
<meta charset="utf-8">
<title>Brask &amp; Partners – Business Card</title>
<link rel="stylesheet" href="https://fonts.googleapis.com/css2?family=Roboto+Condensed:wght@300;400&family=Roboto:wght@400;500&display=swap">
<style>
  :root {
    --page: #ffffff;
    --card: #1f111d;
    --ink-light: #ffffff;
    --ink-soft: #e9e4ea;
    --ink-dark: #2a1a27;
    --band: #ffffff;
    --accent-blue: #1b9ad6;
    --accent-magenta: #b5288c;
    --pattern-a: rgba(60, 40, 80, 0.55);
    --pattern-b: rgba(40, 45, 75, 0.35);
  }
  html, body {
    margin: 0;
    padding: 0;
    width: 1042px;
    height: 1200px;
    overflow: hidden;
    background: var(--page);
  }
  .canvas {
    position: relative;
    width: 1042px;
    height: 1200px;
  }
  .card {
    position: absolute;
    left: 95px;
    width: 788px;
    height: 481px;
    background: var(--card);
    box-shadow: 0 6px 22px rgba(0,0,0,0.35);
    overflow: hidden;
    font-family: "Roboto Condensed", "Arial Narrow", sans-serif;
    color: var(--ink-light);
  }
  .card--front { top: 68px; }
  .card--back { top: 605px; }

  .pattern-area {
    position: absolute;
    left: 445px;
    width: 343px;
    height: 255px;
    background: linear-gradient(120deg, var(--pattern-a) 0%, var(--pattern-b) 55%, rgba(31,17,29,0) 100%);
  }
  .card--front .pattern-area { top: 126px; }
  .card--back .pattern-area { top: 126px; }

  .brand {
    position: absolute;
    display: flex;
    align-items: center;
    white-space: nowrap;
    font-family: "Roboto", "Helvetica Neue", sans-serif;
    font-weight: 400;
    color: var(--ink-light);
  }
  .brand__square {
    background: var(--accent-blue);
    flex: none;
  }
  .card--front .brand {
    left: 50%;
    top: 68px;
    transform: translateX(-50%);
    font-size: 36px;
    gap: 14px;
  }
  .card--front .brand__square { width: 16px; height: 16px; }
  .card--back .brand {
    left: 50%;
    top: 190px;
    transform: translateX(-50%);
    font-size: 64px;
    gap: 24px;
  }
  .card--back .brand__square { width: 28px; height: 28px; }

  .person {
    position: absolute;
    right: 436px;
    top: 237px;
    text-align: right;
  }
  .person__name {
    font-weight: 300;
    font-size: 27px;
    letter-spacing: 0.2px;
    padding-bottom: 5px;
    border-bottom: 2px solid var(--ink-light);
    padding-left: 0;
    min-width: 246px;
    display: inline-block;
  }
  .person__title {
    font-weight: 300;
    font-size: 27px;
    margin-top: 4px;
  }
  .divider {
    position: absolute;
    left: 392px;
    top: 210px;
    width: 1px;
    height: 132px;
    background: linear-gradient(var(--card), #cfc6cf 50%, var(--card));
  }
  .contacts {
    position: absolute;
    left: 434px;
    top: 220px;
    margin: 0;
    padding: 0;
    list-style: none;
  }
  .contacts__item {
    display: flex;
    align-items: center;
    height: 27px;
    font-size: 16.5px;
    font-weight: 400;
    color: var(--ink-soft);
  }
  .contacts__icon {
    width: 18px;
    height: 18px;
    margin-right: 22px;
    flex: none;
  }
  .address-band {
    position: absolute;
    left: 0;
    top: 414px;
    width: 788px;
    height: 30px;
    background: var(--band);
    display: flex;
    align-items: center;
    justify-content: center;
    gap: 10px;
    color: var(--ink-dark);
    font-size: 16.5px;
  }
  .address-band__icon { width: 20px; height: 20px; }
  .web-line {
    position: absolute;
    left: 0;
    width: 100%;
    top: 292px;
    text-align: center;
    font-size: 26px;
    font-weight: 400;
    color: var(--ink-light);
  }
</style>
</head>
<body>
<main class="canvas">

  <section class="card card--front" aria-label="Business card front">
    <div class="pattern-area" role="img" aria-label="Faint grid of dim coloured squares as background decoration"></div>

    <div class="brand">
      <span class="brand__square"></span>
      <span class="brand__name">Brask &amp; Partners</span>
    </div>

    <div class="person">
      <div class="person__name">GERGELY HALMINDO</div>
      <div class="person__title">Managing Director</div>
    </div>

    <div class="divider"></div>

    <ul class="contacts">
      <li class="contacts__item">
        <svg class="contacts__icon" viewBox="0 0 18 18" fill="none" stroke="#e9e4ea" stroke-width="1.1">
          <rect x="2" y="5" width="7" height="12"/><rect x="9" y="1.5" width="7" height="15.5"/>
          <path d="M4 8h3M4 11h3M4 14h3M11 5h3M11 8h3M11 11h3M11 14h3"/>
        </svg>
        Brask and Partners Ltd.
      </li>
      <li class="contacts__item">
        <svg class="contacts__icon" viewBox="0 0 18 18" fill="none" stroke="#e9e4ea" stroke-width="1.2">
          <path d="M4 2l3 3-1.5 2c1 2 3 4 5 5l2-1.5 3 3-2 2C8 15 3 10 2 4z"/>
          <path d="M11 2a5 5 0 0 1 5 5M11 5a2 2 0 0 1 2 2"/>
        </svg>
        +36 30 555 0192
      </li>
      <li class="contacts__item">
        <svg class="contacts__icon" viewBox="0 0 18 18" fill="none" stroke="#e9e4ea" stroke-width="1.2">
          <rect x="2" y="4" width="14" height="10"/><path d="M2 4l7 6 7-6M2 14l5-5M16 14l-5-5"/>
        </svg>
        g.halmindo@braskpartnera.hu
      </li>
      <li class="contacts__item">
        <svg class="contacts__icon" viewBox="0 0 18 18" fill="none" stroke="#e9e4ea" stroke-width="1.1">
          <circle cx="9" cy="9" r="7"/><ellipse cx="9" cy="9" rx="3" ry="7"/><path d="M2 9h14M3.5 5h11M3.5 13h11"/>
        </svg>
        www.braskpartnera.hu
      </li>
    </ul>

    <div class="address-band">
      <svg class="address-band__icon" viewBox="0 0 20 20" fill="none" stroke="#2a1a27" stroke-width="1.2">
        <path d="M10 15s-5-5-5-8.5a5 5 0 0 1 10 0C15 10 10 15 10 15z"/><circle cx="10" cy="6.5" r="1.8"/>
        <path d="M6 13l-4 5h16l-4-5"/>
      </svg>
      <span>1047 Budapest, Ravaszi str. 17/B, Hungary</span>
    </div>
  </section>

  <section class="card card--back" aria-label="Business card back">
    <div class="pattern-area" role="img" aria-label="Faint grid of dim coloured squares as background decoration"></div>

    <div class="brand">
      <span class="brand__square"></span>
      <span class="brand__name">Brask &amp; Partners</span>
    </div>

    <div class="web-line">www.braskpartnera.hu</div>
  </section>

</main>
</body>
</html>
```